One of a kind, 100% Pure & Natural Skincare line needs stunning product label

We need product label design for new natural skincare company called Milo & Tess Skincare. We create luxurious, 100% pure & natural skincare that is free from ingredients that may be potentially irritating to the skin. No toxins, preservatives or additives. Our initial product is Harbor Glow Balm, a nourishing face cream that suits discerning women with mature skin and those with dry/sensitive skin needing extra hydration. Also those that choose to minimize their exposure to environmental toxins. Our brand is simple yet elegant, supporting a holistic, authentic lifestyle and embracing natural skincare.

Target Market(s)

Discerning women with mature skin and those with dry/sensitive skin needing extra hydration. Also those that choose to minimize their exposure to environmental toxins.

Industry/Entity Type

Skin Care Product

Font styles to use
Sans Serif
Script

Colors
f9d9e8
fef1ee

Requirements
Must have
• The Logo.
HARBOR GLOW BALM
EMBRACING NATURAL SKINCARE
Labels must be feminine, simple/minimal yet stylish. Uncluttered yet elegant.
This is a very natural product with minimal ingredients.
Nice to have
• The logo can be incorporated in to the label, or It can be left separate as a sticker on top of the jar. The product is a firm balm consistency and is in frosted glass jars with matt silver lids.
Jar height is 45mm, width is 60mm.
Label height: 28mm and length 185mm
Should not have
• Natural or farmers market type theme. No Bold/loud lettering.

```html
<!DOCTYPE html>
<html lang="en">
<head>
<meta charset="utf-8">
<title>Milo &amp; Tess Skincare – Harbor Glow Balm Label</title>
<link href="https://fonts.googleapis.com/css2?family=Montserrat:wght@400;500;600;700&family=Great+Vibes&display=swap" rel="stylesheet">
<style>
  :root {
    --page-bg: #ffffff;
    --label-light: #f2f2f3;
    --label-mid: #d9d9db;
    --label-dark: #c6c6c8;
    --ink: #1e1e1e;
    --ink-soft: #2b2b2b;
    --rule: #2a2a2a;
    --bb-box: #fbfbfb;
    --blush: #f2a8b4;
    --script-ink: #c9737f;
  }
  html, body {
    margin: 0;
    padding: 0;
    width: 1200px;
    height: 1200px;
    overflow: hidden;
    background: var(--page-bg);
    font-family: "Montserrat", sans-serif;
    color: var(--ink);
  }
  .canvas {
    position: relative;
    width: 1200px;
    height: 1200px;
  }
  .label {
    position: absolute;
    left: 20px;
    top: 512px;
    width: 1160px;
    height: 176px;
    border-radius: 6px;
    background: linear-gradient(90deg,
      var(--label-mid) 0%,
      var(--label-light) 14%,
      var(--label-dark) 30%,
      var(--label-light) 50%,
      var(--label-mid) 66%,
      var(--label-light) 82%,
      var(--label-mid) 100%);
    box-shadow: 0 1px 3px rgba(0,0,0,0.12);
  }
  .rule {
    height: 1px;
    background: var(--rule);
    border-radius: 1px;
  }

  .panel-info {
    position: absolute;
    left: 16px;
    top: 24px;
    width: 240px;
    font-size: 11px;
    line-height: 13.4px;
  }
  .panel-info p { margin: 0; }
  .panel-info strong { font-weight: 700; }
  .panel-info .rule { width: 222px; margin: 8px 0; }

  .panel-front {
    position: absolute;
    left: 450px;
    top: 10px;
    width: 320px;
    text-align: center;
  }
  .brand {
    display: inline-flex;
    align-items: center;
    gap: 8px;
    margin-top: 6px;
    font-size: 16px;
    line-height: 20px;
    font-weight: 500;
    letter-spacing: 0.5px;
    color: var(--ink-soft);
  }
  .brand-dot {
    width: 10px;
    height: 10px;
    border-radius: 50%;
    background: var(--blush);
  }
  .script-tagline {
    margin: 2px 0 0;
    font-family: "Great Vibes", cursive;
    font-size: 19px;
    line-height: 20px;
    color: var(--script-ink);
  }
  .tagline {
    margin: 8px 0 0;
    font-size: 11px;
    line-height: 14px;
    letter-spacing: 0.4px;
  }
  .product-name {
    margin: 3px 0 0;
    font-size: 20px;
    line-height: 24px;
    font-weight: 600;
    letter-spacing: 0.8px;
  }
  .panel-front .rule { width: 186px; margin: 5px auto 0; }
  .meta {
    margin: 7px 0 0;
    font-size: 9px;
    line-height: 11px;
    letter-spacing: 0.3px;
  }

  .panel-directions {
    position: absolute;
    left: 876px;
    top: 22px;
    width: 230px;
    font-size: 11px;
    line-height: 13.2px;
  }
  .panel-directions p { margin: 0; }
  .panel-directions strong { font-weight: 700; }
  .panel-directions .origin { margin-top: 5px; }
  .badges {
    display: block;
    margin-top: 5px;
  }
  .panel-directions .rule { width: 186px; margin: 5px 0 6px; }

  .bb-strip {
    position: absolute;
    left: 1122px;
    top: 13px;
    width: 22px;
    height: 146px;
    background: var(--bb-box);
  }
  .bb-strip span {
    position: absolute;
    left: 16px;
    bottom: 8px;
    font-size: 11px;
    transform: rotate(-90deg);
    transform-origin: left bottom;
  }
</style>
</head>
<body>
<main class="canvas">
  <section class="label" aria-label="Harbor Glow Balm jar label">

    <div class="panel-info">
      <p><strong>INGREDIENTS:</strong> tallow from pasture raised goats, frankincense, sandalwood &amp; myrrh essential oils.</p>
      <div class="rule"></div>
      <p><strong>CAUTION:</strong> Keep out of reach of children. If pregnant or breastfeeding, consult your healthcare practitioner. Avoid contact with eyes &amp; sensitive areas.</p>
      <p>Allergy patch test recommended. If irritation occurs, discontinue use.</p>
    </div>

    <div class="panel-front">
      <div class="brand"><span class="brand-dot"></span>Milo &amp; Tess Skincare</div>
      <p class="script-tagline">Embracing Natural Skincare</p>
      <p class="tagline">100% PURE &amp; NATURAL</p>
      <h1 class="product-name">HARBOR GLOW BALM</h1>
      <div class="rule"></div>
      <p class="meta">FOR DRY &amp; SENSITIVE SKIN &nbsp;·&nbsp; 50ml</p>
    </div>

    <div class="panel-directions">
      <p><strong>DIRECTIONS:</strong></p>
      <p>Soften small amount in palm of hand &amp; gently massage into skin as often as required.</p>
      <p>Store below 25°C</p>
      <p class="origin">MADE IN AUSTRALIA</p>
      <svg class="badges" width="180" height="32" viewBox="0 0 180 32" aria-label="Product certification badges">
        <circle cx="14" cy="18" r="12" fill="none" stroke="#1e1e1e" stroke-width="1.4"/>
        <circle cx="14" cy="18" r="7" fill="#1e1e1e"/>
        <circle cx="48" cy="18" r="12" fill="none" stroke="#1e1e1e" stroke-width="1.4"/>
        <circle cx="48" cy="18" r="6" fill="none" stroke="#1e1e1e" stroke-width="1.4"/>
        <circle cx="82" cy="18" r="12" fill="none" stroke="#1e1e1e" stroke-width="1.4"/>
        <polygon points="116,5 130,30 102,30" fill="#1e1e1e"/>
        <rect x="142" y="16" width="26" height="14" rx="3" fill="none" stroke="#1e1e1e" stroke-width="1.4"/>
        <rect x="140" y="6" width="26" height="5" rx="1.5" fill="none" stroke="#1e1e1e" stroke-width="1.4" transform="rotate(-22 153 9)"/>
      </svg>
      <div class="rule"></div>
      <p>info@milotessskincare.com.au</p>
    </div>

    <div class="bb-strip"><span>BB:</span></div>
  </section>
</main>
</body>
</html>
```